Label for Sports Nutrition Supplement

I need a label design for a pre-workout sports nutrition supplement. A pre-workout supplement helps increase energy, strength, stamina, and endurance.

The name of the company is Tallcrest Nutrition

The demographic is males between the ages of 18-35 who like to workout to stay in shape.

I'd like to see designs that have a red (#FF0000), black, and white color. The container will be black and similar to this one:

https://www.shopvarlo.example/Dunmere-Vigor-Works-Workout-Supplement/item/Q4827KXPLM

Some designs that caught my attention are:

a) http://www.brivello-fizz.example/stories/brivello-zero-sugar-new-and-improved-sugar-free-brivello-launches-this-summer

b) The Brivo Zero can (2nd can from the left side) http://dailyhalden.example/2015/03/09/brivello-is-trialling-new-unified-packaging-and-its-totally-different-4817362/

c) https://www.shopvarlo.example/KRV-Clinically-Pulsevane-Testosterone-Enhancing/item/Z318WQRTNB

d) https://www.shopvarlo.example/OLDEN-SURGE-Pre-Workout-Non-Habit-Forming-All-Natural/item/M562HJDKEV

e) http://www.craftplume.example/design-gallery/bison-pre-workout-48213

f) https://www.wrapjournal.example/features/comment/history-of-the-world-in-52-packs-10-the-dunhaven-flip-top-box-29-09-2015

This label should do the following 5 things:

a. Stand out
b. Be simple
c. Pass the 5 year old test
d. Trigger emotional engagement
e. Create iconic assets

You can read more about what these 5 elements mean here... https://www.tradelumen.example/sites/onmarketing/2014/07/23/the-five-things-product-packaging-must-do/

The final design should communicate increased physical performance.

The instructions of the label are attached and include the elements that need to appear in each section of the label.

The company logo is attached.

The barcode is attached.

Thank you.

Target Market(s)

Industry/Entity Type

Supplement

Font styles to use
Serif
Sans Serif

Colors
ec1f27
ffffff
000000

Requirements
Must have
• This label should do the following 5 things:
• a. Stand out
• b. Be simple
• c. Pass the 5 year old test
• d. Trigger emotional engagement
• e. Create iconic assets
• You can read more about what these 5 elements mean here... https://www.tradelumen.example/sites/onmarketing/2014/07/23/the-five-things-product-packaging-must-do/
• The final design should communicate increased physical performance.
• Red color should be this color of red... #FF0000
• Using a blue color is NOT a must have, BUT if you decide to use a blue color, use this color of blue ... #0019A8
Nice to have
• OPTIONAL >> These effects caught my attention and are 100% OPTIONAL. Use them only if you feel it will make a better design.
• 1) A text that goes from small to large, such as the GRAVELOX text shown here... https://www.gravelox-cereal.example/
• 2) A text that is vertical, such as the VAMBR text shown here...
• https://www.vambr-fit.example

```html
<!DOCTYPE html>
<html lang="en">
<head>
<meta charset="utf-8">
<title>Tallcrest Nutrition – DRIVEN Pre-Workout Label</title>
<link href="https://fonts.googleapis.com/css2?family=Anton&family=Oswald:wght@400;500;700&family=Roboto:wght@400;700&family=Tinos:wght@400;700&display=swap" rel="stylesheet">
<style>
  :root{
    --red:#ec1f27;
    --red-deep:#b8151b;
    --black:#0c0c0c;
    --charcoal:#1c1c1c;
    --white:#ffffff;
    --paper:#f4f4f4;
    --bg:#d9d9d9;
  }
  *{box-sizing:border-box;margin:0;padding:0}
  html,body{width:1200px;height:960px;overflow:hidden;background:var(--bg)}
  .canvas{position:relative;width:1200px;height:960px}
  .label{position:absolute;left:30px;top:200px;width:1140px;height:560px;overflow:hidden;
    background:linear-gradient(180deg,var(--charcoal),var(--black));font-family:"Roboto",sans-serif}
  .label-bands{position:absolute;inset:0}
  .abs{position:absolute}

  /* left panel */
  .about{left:24px;top:78px;width:330px;color:var(--white);font-size:9.2px;line-height:1.4;text-align:justify}
  .about p{margin-bottom:8px}
  .about .hl{color:var(--red);font-weight:700}
  .about .tagline{margin-top:14px;font-size:9.6px;font-weight:700;text-align:left}
  .distributor{left:24px;top:432px;color:var(--black);font-family:"Oswald",sans-serif}
  .distributor h3{font-size:16px;font-weight:500}
  .distributor p{font-size:9.5px;font-weight:700;line-height:1.3;font-family:"Roboto",sans-serif}
  .divider{left:218px;top:430px;width:1px;height:58px;background:var(--black)}
  .flag{left:248px;top:430px;width:50px;height:30px;background:linear-gradient(180deg,#b22234 0 50%,#3c3b6e 50% 100%)}
  .made{left:238px;top:466px;font-size:9px;font-weight:700;color:var(--white)}
  .disclaimer{left:20px;top:500px;width:330px;padding:6px 12px;border:2px solid var(--black);border-radius:16px;
    font-size:8.5px;font-style:italic;color:var(--white);line-height:1.3}

  /* center panel */
  .brand{left:470px;top:38px;display:flex;align-items:center;gap:10px}
  .brand-dot{width:38px;height:38px;border-radius:50%;background:var(--red)}
  .brand-name{font-family:"Oswald",sans-serif;font-weight:700;font-size:20px;color:var(--white);letter-spacing:1px;text-transform:uppercase}
  .product-name{left:404px;top:84px;font-family:"Anton",sans-serif;font-size:108px;line-height:1;color:var(--red);
    letter-spacing:2px;transform:rotate(-4deg);transform-origin:left bottom}
  .category{left:410px;top:260px;font-family:"Oswald",sans-serif;font-weight:500;font-size:34px;line-height:1;color:var(--black);
    transform:rotate(-4deg);transform-origin:left top}
  .benefits{left:414px;top:306px;list-style:none;font-family:"Oswald",sans-serif;font-size:16px;line-height:1.45;color:var(--black);
    transform:rotate(-4deg);transform-origin:left top}
  .benefits li::before{content:"▶";color:var(--white);margin-right:8px;font-size:12px}
  .fruit{left:712px;top:226px;width:50px;height:50px;border-radius:50%;background:radial-gradient(circle at 40% 40%,#f6a21b,#d8431a)}
  .flavor{left:640px;top:284px;width:150px;height:32px;background:var(--black);transform:rotate(-9deg);
    display:flex;align-items:center;justify-content:center;font-family:"Oswald",sans-serif;font-weight:700;font-style:italic;font-size:16px;color:var(--white);letter-spacing:1px}
  .type{left:410px;top:402px;font-family:"Oswald",sans-serif;font-weight:500;font-size:36px;line-height:1;color:var(--white);
    transform:rotate(-8deg);transform-origin:left top;white-space:nowrap}
  .servings{left:560px;top:452px;width:220px;height:44px;background:var(--black);transform:rotate(-8deg);
    display:flex;align-items:center;justify-content:center;font-family:"Oswald",sans-serif;font-weight:500;font-size:32px;line-height:1;color:var(--red)}
  .netweight{left:584px;top:528px;font-family:"Oswald",sans-serif;font-size:13px;line-height:1;color:var(--black);
    transform:rotate(-8deg);transform-origin:left top;white-space:nowrap}

  /* right panel */
  .facts{left:806px;top:92px;width:300px;background:var(--paper);border:2px solid var(--black);padding:8px 10px;
    font-family:"Tinos",serif;font-size:8.4px;color:var(--black);line-height:1.3}
  .facts h4{font-size:11px;font-weight:700}
  .facts table{width:100%;border-collapse:collapse;margin-top:4px}
  .facts td,.facts th{padding:0 2px;font-weight:400;text-align:left}
  .facts th.r,.facts td.r{text-align:right}
  .facts .rule{border-top:2px solid var(--black)}
  .facts .note{margin-top:6px;border-top:1px solid var(--black);padding-top:4px}
  .directions{left:806px;top:352px;width:300px;font-size:9.2px;color:var(--white);line-height:1.35;transform:rotate(-3deg)}
  .directions b{color:var(--black);font-weight:700}
  .directions ol{list-style:none;margin-top:3px}
  .directions li{display:flex;gap:6px;margin-bottom:3px}
  .directions .n{flex:none;width:13px;height:13px;border-radius:50%;background:var(--black);color:var(--white);font-size:8px;display:flex;align-items:center;justify-content:center}
  .warning{left:806px;top:454px;width:300px;padding:6px 10px 6px 30px;border:2px solid var(--black);border-radius:16px;
    font-size:7.6px;color:var(--white);line-height:1.3;transform:rotate(-3deg)}
  .warning svg{position:absolute;left:9px;top:50%;margin-top:-8px}
</style>
</head>
<body>
<div class="canvas">
  <div class="label">
    <svg class="label-bands" width="1140" height="560" viewBox="0 0 1140 560" aria-hidden="true">
      <polygon points="0,418 395,400 395,256 780,206 1140,206 1140,548 0,556" fill="var(--red)"/>
    </svg>

    <!-- left panel -->
    <div class="abs about">
      <p><span class="hl">DRIVEN</span> is powdered energy. Having active ingredients whose dosages are clinically effective and have been scientifically proven to enhance energy, focus, and performance, this powerful pre-workout formula will help you achieve peak performance.*</p>
      <p>Each serving of DRIVEN helps promote strength (pumps), stamina (performance), and endurance (mental focus) so you can lift one last rep or run an extra mile. Push yourself to the limit with increased alertness and improved concentration, all while recovering faster from adequate hydration and electrolyte balance. Its unique blend of ingredients help you power through even the most intense workouts.*</p>
      <p>DRIVEN has NO unnecessary fillers, artificial colors, preservatives, banned substances, or proprietary blends. The dosages are fully disclosed so you know exactly what you're ingesting. Its mixability means 100% absorption.</p>
      <p>If you're looking for an explosive pre-workout that drives performance and supports your fitness goals – whether getting lean or building muscle – DRIVEN is for you. It's the obvious choice, whatever your level. Take it 30 minutes before exercise for a workout like no other!</p>
      <p class="tagline">DRIVEN - For peak performance.</p>
    </div>
    <div class="abs distributor">
      <h3>Distributed by:</h3>
      <p>Tallcrest Nutrition<br>Ridgeford, WY 82990<br>Shop tallcrestnutrition.example</p>
    </div>
    <div class="abs divider"></div>
    <div class="abs flag" role="img" aria-label="United States flag"></div>
    <div class="abs made">MADE IN USA</div>
    <div class="abs disclaimer">* These statements have not been evaluated by the Food and Drug Administration. This product is not intended to diagnose, treat, cure, or prevent any disease.</div>

    <!-- center panel -->
    <div class="abs brand"><span class="brand-dot"></span><span class="brand-name">Tallcrest Nutrition</span></div>
    <div class="abs product-name">DRIVEN</div>
    <div class="abs category">PRE-WORKOUT</div>
    <ul class="abs benefits">
      <li>STRENGTH (PUMPS)</li>
      <li>STAMINA (PERFORMANCE)</li>
      <li>ENDURANCE (FOCUS)</li>
    </ul>
    <div class="abs fruit" role="img" aria-label="Illustration of a bunch of mixed fruit"></div>
    <div class="abs flavor">FRUIT PUNCH</div>
    <div class="abs type">DIETARY SUPPLEMENT</div>
    <div class="abs servings">20 SERVINGS</div>
    <div class="abs netweight">NET WEIGHT: 444 GRAMS (0.98 LB)</div>

    <!-- right panel -->
    <div class="abs facts">
      <h4>Supplement Facts</h4>
      <div>Serving Size: 2 Scoops (22.19 g)</div>
      <div>Servings per Container: 20 (40 Scoops)</div>
      <table>
        <tr class="rule"><th></th><th class="r">Amount per Serving</th><th class="r">% Daily Value</th></tr>
        <tr><td>Potassium (as Potassium Citrate)</td><td class="r">376 mg</td><td class="r">11%</td></tr>
        <tr><td>Sodium (as Sodium Chloride)</td><td class="r">138 mg</td><td class="r">6%</td></tr>
        <tr><td>Calcium (as Dicalcium Phosphate)</td><td class="r">80 mg</td><td class="r">8%</td></tr>
        <tr class="rule"><td>L-Citrulline DL-Malate</td><td class="r">8250 mg</td><td class="r">**</td></tr>
        <tr><td>Beta Alanine</td><td class="r">4500 mg</td><td class="r">**</td></tr>
        <tr><td>Betaine Anhydrous</td><td class="r">2500 mg</td><td class="r">**</td></tr>
        <tr><td>D-Aspartic Acid</td><td class="r">2000 mg</td><td class="r">**</td></tr>
        <tr><td>Caffeine Anhydrous</td><td class="r">350 mg</td><td class="r">**</td></tr>
      </table>
      <div class="note">** Daily Value Not Established. &nbsp; % Daily Value Based on a 2000 Calorie Diet</div>
      <div class="note">Other Ingredients: Natural &amp; Artificial Flavors, Sucralose, Citric Acid, Silica<br>Contains NO: wheat, gluten, soy, dairy, preservatives, artificial colors, fillers.<br>Suitable for vegans and vegetarians.</div>
    </div>
    <div class="abs directions">
      <b>DIRECTIONS:</b> To determine tolerance, mix one
      <ol>
        <li><span class="n">1</span><span>scoop with 11 ounces (325 ml) of water and take 15-30 minutes before exercise. After tolerance has been determined, take 1-2 scoops 15-30 minutes before exercise. Use two</span></li>
        <li><span class="n">2</span><span>scoops for intense exercise, including cardio lasting more than 45 minutes.</span></li>
      </ol>
    </div>
    <div class="abs warning">
      <svg width="16" height="16" viewBox="0 0 16 16" aria-hidden="true"><path d="M8 1 L15 15 H1 Z" fill="none" stroke="var(--black)" stroke-width="1.5"/><path d="M8 6 V10 M8 12 V13" stroke="var(--black)" stroke-width="1.5"/></svg>
      WARNING: Do not use if you are pregnant, nursing, under the age of 18, sensitive to caffeine, or have a medical condition. Consult a physician before use. Use only as directed. Store in a cool, dry place. Keep out of reach of children.
    </div>
  </div>
</div>
</body>
</html>
```